Business Card and Letterhead for Nurlo - modern real estate business

I need a double sided business card design for Nurlo. Please see business card brief here https://papers.trelvimo.net/sheet/q/7XrTbaLeZpMmQ2uWvd9HkCj4yNoEfsGi3lRtAz_pk/view?mode=shared

Please feel free to design the business cards however you feel best. I am happy to give some creative freedoms and then provide feedback from there.

Please then also create a letterhead to match the business card design

Colors

Designer to choose colors to be used in the design.

Requirements
Must have
• Must be a modern, elegant business card which looks very professional

```html
<!DOCTYPE html>
<html lang="en">
<head>
<meta charset="utf-8">
<title>Nurlo Business Card</title>
<link href="https://fonts.googleapis.com/css2?family=Montserrat:wght@400;500;700&display=swap" rel="stylesheet">
<style>
  :root {
    --brand-red: #e31e26;
    --ink-black: #231f20;
    --text-grey: #4a4a4a;
    --paper: #ffffff;
    --backdrop: #e9e9e9;
    --photo-top: #b9b2aa;
    --photo-bottom: #2f3134;
  }
  * { margin: 0; padding: 0; box-sizing: border-box; }
  html, body { width: 1200px; height: 801px; overflow: hidden; }
  body {
    background: var(--backdrop);
    font-family: "Montserrat", sans-serif;
    position: relative;
  }
  .card {
    position: absolute;
    top: 246px;
    width: 540px;
    height: 309px;
    overflow: hidden;
    box-shadow: 0 6px 18px rgba(0,0,0,0.18);
  }
  .card-front { left: 40px; background: var(--paper); }
  .card-back { left: 620px; background: var(--ink-black); display: flex; align-items: center; justify-content: center; }

  .front-art { position: absolute; inset: 0; }

  .front-info { position: absolute; left: 34px; top: 40px; }
  .brand-name {
    font-weight: 700;
    font-size: 40px;
    letter-spacing: 5px;
    color: var(--brand-red);
    line-height: 1;
  }
  .agent-name {
    margin-top: 26px;
    font-weight: 700;
    font-size: 19px;
    color: var(--brand-red);
  }
  .agent-title {
    margin-top: 3px;
    font-size: 11px;
    color: var(--text-grey);
  }
  .agent-address {
    margin-top: 12px;
    font-size: 11px;
    line-height: 1.45;
    color: var(--text-grey);
  }
  .contact-list { margin-top: 10px; list-style: none; }
  .contact-item {
    display: flex;
    align-items: center;
    gap: 8px;
    font-size: 11px;
    line-height: 1.7;
    color: var(--text-grey);
  }
  .contact-icon { width: 10px; height: 10px; flex: none; }

  .back-brand {
    font-weight: 700;
    font-size: 84px;
    letter-spacing: 10px;
    color: var(--brand-red);
    line-height: 1;
  }
</style>
</head>
<body>
  <section class="card card-front">
    <svg class="front-art" width="540" height="309" viewBox="0 0 540 309">
      <defs>
        <linearGradient id="portrait-tone" x1="0" y1="0" x2="0" y2="1">
          <stop offset="0" stop-color="var(--photo-top)"/>
          <stop offset="0.45" stop-color="var(--photo-bottom)"/>
          <stop offset="1" stop-color="var(--photo-bottom)"/>
        </linearGradient>
      </defs>
      <rect class="agent-portrait" x="300" y="34" width="215" height="250" rx="4" fill="url(#portrait-tone)" role="img" aria-label="Portrait photo of the agent in a dark jacket"/>
      <path class="swoosh-line" d="M150 297 C 290 258, 400 158, 540 83" fill="none" stroke="var(--ink-black)" stroke-width="3"/>
      <path class="swoosh-gap" d="M150 311 C 290 272, 400 172, 540 97 L540 309 L150 309 Z" fill="var(--paper)"/>
      <path class="swoosh-band" d="M150 318 C 290 279, 400 179, 540 104 L540 309 L150 309 Z" fill="var(--brand-red)"/>
    </svg>

    <div class="front-info">
      <div class="brand-name">NURLO</div>
      <div class="agent-name">Dana Morrell</div>
      <div class="agent-title">Licenced Real Estate Agent</div>
      <div class="agent-address">PO Box 1190<br>Larkfield NSW 2790</div>
      <ul class="contact-list">
        <li class="contact-item">
          <svg class="contact-icon" viewBox="0 0 10 10"><path d="M2 0.5 L3.6 2.8 L2.6 3.8 C3.2 5.2 4.8 6.8 6.2 7.4 L7.2 6.4 L9.5 8 L8.3 9.5 C4.5 9.2 0.8 5.5 0.5 1.7 Z" fill="var(--brand-red)"/></svg>
          0412 583 907
        </li>
        <li class="contact-item">
          <svg class="contact-icon" viewBox="0 0 10 10"><rect x="0.5" y="1.5" width="9" height="7" fill="var(--brand-red)"/><path d="M1 2 L5 5.5 L9 2" fill="none" stroke="var(--paper)" stroke-width="1"/></svg>
          dana@nurlo.com
        </li>
        <li class="contact-item">
          <svg class="contact-icon" viewBox="0 0 10 10"><circle cx="5" cy="5" r="4.5" fill="var(--brand-red)"/><path d="M0.5 5 H9.5 M5 0.5 C2.5 3 2.5 7 5 9.5 M5 0.5 C7.5 3 7.5 7 5 9.5" fill="none" stroke="var(--paper)" stroke-width="0.7"/></svg>
          www.nurlo.com
        </li>
      </ul>
    </div>
  </section>

  <section class="card card-back">
    <div class="back-brand">NURLO</div>
  </section>
</body>
</html>
```